Briefpapier, Visitenkarten, Bindemappe, Brieumschläge....
Zielgruppe
Steuerberatung vorwiegen für Unternehmer
Aufgabenstellung
Ein Logo ist bereits vorhanden (siehe Analgen) kann aber gerne auch bei einer guten Idee modernisiert werden. Ganz ein neues Logo möchte ich meinen Kunden jedoch ersparen, da ich es erst von zwei Jahren gewechselt habe. Grundfarbe grün wie Pantone 2293 C.
Als Anhaltspunkt was derzeit bei im Einsatz ist, habe ich die entsprechenden Dateien hochgeladen.

```html
<!DOCTYPE html>
<html lang="de">
<head>
<meta charset="utf-8">
<title>Steuerberater Konrad Albers – Geschäftsausstattung</title>
<link href="https://fonts.googleapis.com/css2?family=Barlow+Semi+Condensed:wght@400;500;600&display=swap" rel="stylesheet">
<style>
:root{
  --green:#8cc700;
  --green-tint:#f3f8e6;
  --dark:#3c4442;
  --text:#555a58;
  --faint:#f6f6f6;
  --paper:#ffffff;
  --edge:#d4d4d4;
}
*{box-sizing:border-box;margin:0;padding:0}
html,body{width:973px;height:1200px;overflow:hidden;background:var(--paper)}
body{position:relative;font-family:"Barlow Semi Condensed",sans-serif;color:var(--text)}
.abs{position:absolute}

/* Wortmarke */
.brand{display:flex;align-items:center;gap:10px}
.brand-square{background:var(--green);flex:none}
.brand-name{font-weight:600;text-transform:uppercase;line-height:1;color:var(--dark);letter-spacing:.02em}
.brand-name span{display:block}
.brand--hero{left:338px;top:37px}
.brand--hero .brand-square{width:56px;height:56px}
.brand--hero .brand-name{font-size:25px}
.brand--hero .brand-name span+span{font-size:30px;margin-top:2px}

/* Briefbogen */
.letterhead{left:245px;top:121px;width:482px;height:682px;background:var(--paper);box-shadow:0 0 3px rgba(0,0,0,.25);overflow:hidden}
.bar{position:absolute;left:0;right:0;height:10px;background:var(--green)}
.bar--top{top:0}.bar--bottom{bottom:0}
.letterhead .brand{left:56px;top:67px}
.letterhead .brand-square{width:30px;height:30px}
.letterhead .brand-name{font-size:13px}
.letterhead .brand-name span+span{font-size:15px}
.sender-line{left:57px;top:127px;font-size:6px;color:#222;white-space:nowrap}
.sender-line b{color:var(--green);font-weight:600}
.contact{border-left:1px solid var(--green);padding-left:5px;font-size:6.4px;line-height:1.25}
.contact .name{color:var(--green);font-weight:600;font-size:7px}
.contact .role{color:var(--green);margin-bottom:7px}
.contact p{margin-bottom:7px}
.contact p:last-child{margin-bottom:0}
.letterhead .contact{left:390px;top:30px;height:88px}
.backdrop{left:0;right:0;top:194px;bottom:10px;background:var(--faint)}

/* Visitenkarten */
.card{width:196px;height:126px;box-shadow:0 0 3px rgba(0,0,0,.3)}
.card--front{left:281px;top:830px;background:var(--dark);display:flex;flex-direction:column;align-items:center;justify-content:center;gap:8px}
.card--front .brand{flex-direction:column;gap:8px}
.card--front .brand-square{width:30px;height:30px}
.card--front .brand-name{color:var(--green);font-size:12px;text-align:center}
.card--front .brand-name span+span{font-size:14px}
.card--back{left:495px;top:830px;background:var(--paper)}
.card--back .brand-square{left:37px;top:47px;width:32px;height:32px;background:var(--green)}
.card--back .contact{left:100px;top:20px;border-left:none;padding-left:0}

/* Notizblock */
.notepad{left:326px;top:995px;width:165px;height:165px;background:var(--paper);border:1px solid #333}
.notepad-band{left:0;right:0;top:0;height:44px;background:var(--green-tint)}
.notepad .brand{left:32px;top:48px;gap:5px}
.notepad .brand-square{width:19px;height:19px}
.notepad .brand-name{font-size:7.5px}
.notepad .brand-name span+span{font-size:8.5px}
.notepad-foot{left:0;right:0;bottom:0;height:11px;background:var(--green);color:#fff;font-size:5px;font-weight:600;text-align:center;line-height:11px}

/* Ordnerrücken-Etiketten */
.spine{width:48px;height:104px}
.spine--a{left:519px;top:1031px;background:var(--paper);box-shadow:0 0 3px rgba(0,0,0,.3);border-left:5px solid var(--green);border-right:5px solid var(--green)}
.spine--b{left:578px;top:1031px}
.spine-shape{position:absolute;left:0;top:0;width:48px;height:104px;overflow:visible}
.spine-name{position:absolute;left:50%;top:4px;width:18px;margin-left:-9px;height:54px;
  writing-mode:vertical-rl;transform:rotate(180deg);
  font-weight:600;text-transform:uppercase;color:var(--dark);line-height:9px;font-size:6px;letter-spacing:.05em;text-align:left}
.spine-name span{display:block}
.spine-name span+span{font-size:6.5px;letter-spacing:.04em}
.spine-square{position:absolute;left:50%;top:60px;width:12px;height:12px;margin-left:-6px;background:var(--green)}
.spine--a .spine-name{margin-left:-14px}
.spine--a .spine-square{margin-left:-11px}
</style>
</head>
<body>

<div class="brand brand--hero abs">
  <div class="brand-square"></div>
  <div class="brand-name"><span>Steuerberater</span><span>Konrad Albers</span></div>
</div>

<section class="letterhead abs" aria-label="Briefbogen">
  <div class="bar bar--top"></div>
  <div class="brand abs">
    <div class="brand-square"></div>
    <div class="brand-name"><span>Steuerberater</span><span>Konrad Albers</span></div>
  </div>
  <div class="sender-line abs"><b>Konrad Albers</b> Steuerberater • Lindenweg 4 • 86150 Musterstadt</div>
  <div class="contact abs">
    <div class="name">Konrad Albers</div>
    <div class="role">Steuerberater</div>
    <p>Lindenweg 4<br>86150 Musterstadt</p>
    <p>Tel.: 0821 / 555 20 – 10<br>Fax: 0821 / 555 20 – 11</p>
    <p>info@kanzlei-albers.de<br>www.kanzlei-albers.de</p>
  </div>
  <div class="backdrop abs" role="img" aria-label="Dezente hellgraue Hintergrundfläche"></div>
  <div class="bar bar--bottom"></div>
</section>

<div class="card card--front abs">
  <div class="brand">
    <div class="brand-square"></div>
    <div class="brand-name"><span>Steuerberater</span><span>Konrad Albers</span></div>
  </div>
</div>

<div class="card card--back abs">
  <div class="brand-square abs"></div>
  <div class="contact abs">
    <div class="name">Konrad Albers</div>
    <div class="role">Steuerberater</div>
    <p>Lindenweg 4<br>86150 Musterstadt</p>
    <p>Tel.: 0821 / 555 20 – 10<br>Fax: 0821 / 555 20 – 11</p>
    <p>info@kanzlei-albers.de<br>www.kanzlei-albers.de</p>
  </div>
</div>

<div class="notepad abs">
  <div class="notepad-band abs"></div>
  <div class="brand abs">
    <div class="brand-square"></div>
    <div class="brand-name"><span>Steuerberater</span><span>Konrad Albers</span></div>
  </div>
  <div class="notepad-foot abs">0821 / 555 20 – 10 • www.kanzlei-albers.de</div>
</div>

<div class="spine spine--a abs">
  <div class="spine-name"><span>Steuerberater</span><span>Konrad Albers</span></div>
  <div class="spine-square"></div>
</div>

<div class="spine spine--b abs">
  <svg class="spine-shape" viewBox="0 0 48 104" aria-hidden="true">
    <polygon points="0,0 48,0 48,60 8,104 0,104" fill="#ffffff" stroke="#d4d4d4" stroke-width="1"/>
    <rect x="0" y="0" width="5" height="104" fill="#8cc700"/>
    <rect x="43" y="0" width="5" height="60" fill="#8cc700"/>
  </svg>
  <div class="spine-name"><span>Steuerberater</span><span>Konrad Albers</span></div>
  <div class="spine-square"></div>
</div>

</body>
</html>
```